Launching new podcast and need artwork

we are two guys in our early 40's from east Texas who are starting a podcast around personal finance.

The title of the podcast will be "Ledger Gripes" and the subtitle will be "Financial hacks with some southern charm"

We own the company boundlessdaysplanning.example and will be using the podcast as a lead generation for our primary business of financial coaching.

Target Market(s)

Male 35-45 years old

Industry/Entity Type

Personal finance

Requirements
Nice to have
• Rugged or rustic feel would fit our personas

```html
<!DOCTYPE html>
<html lang="en">
<head>
<meta charset="utf-8">
<title>Ledger Gripes Podcast Cover</title>
<link rel="stylesheet" href="https://fonts.googleapis.com/css2?family=Poppins:wght@400;700;800;900&family=Kaushan+Script&display=swap">
<style>
  :root {
    --navy-deep: #0a1630;
    --navy-mid: #0c2a66;
    --blue-low: #0f3f9e;
    --blue-floor: #1656c8;
    --white: #ffffff;
    --lime: #b2ff59;
    --ink: #1c2f52;
  }
  * { margin: 0; padding: 0; box-sizing: border-box; }
  html, body { width: 1200px; height: 1200px; overflow: hidden; background: var(--white); }
  .cover { display: block; width: 1200px; height: 1200px; }
  .title-top { font-family: "Poppins", sans-serif; font-weight: 900; fill: var(--white); }
  .title-bottom { font-family: "Poppins", sans-serif; font-weight: 900; fill: var(--lime); }
  .tagline { font-family: "Poppins", sans-serif; font-weight: 700; fill: var(--ink); letter-spacing: 4px; }
  .label-podcast { font-family: "Poppins", sans-serif; font-weight: 400; fill: var(--white); }
  .label-with { font-family: "Kaushan Script", cursive; fill: var(--white); }
  .hosts { font-family: "Poppins", sans-serif; font-weight: 800; fill: var(--lime); }
</style>
</head>
<body>
<svg class="cover" viewBox="0 0 1200 1200" xmlns="http://www.w3.org/2000/svg" role="img" aria-label="Ledger Gripes podcast cover">
  <defs>
    <linearGradient id="sky" x1="0" y1="0" x2="0" y2="1">
      <stop offset="0" stop-color="var(--navy-deep)"/>
      <stop offset=".5" stop-color="var(--navy-mid)"/>
      <stop offset="1" stop-color="var(--blue-low)"/>
    </linearGradient>
    <linearGradient id="chartGlow" x1="0" y1="0" x2="0" y2="1">
      <stop offset="0" stop-color="var(--navy-mid)" stop-opacity="0"/>
      <stop offset=".75" stop-color="var(--blue-low)" stop-opacity=".8"/>
      <stop offset=".86" stop-color="var(--blue-floor)"/>
      <stop offset="1" stop-color="var(--blue-low)"/>
    </linearGradient>
  </defs>

  <rect class="backdrop" width="1200" height="1200" fill="url(#sky)"/>

  <rect class="market-chart-backdrop" x="0" y="560" width="1200" height="640" fill="url(#chartGlow)"
        role="img" aria-label="Faint stock market bar and line chart fading into a glowing blue floor"/>

  <text class="title-top" x="80" y="292" font-size="250" textLength="1030" lengthAdjust="spacingAndGlyphs">LEDGER</text>
  <text class="title-bottom" x="88" y="553" font-size="318" textLength="1038" lengthAdjust="spacingAndGlyphs">GRIPES</text>

  <rect class="tagline-pill" x="76" y="600" width="1048" height="70" rx="18" fill="var(--white)"/>
  <text class="tagline" x="600" y="649" font-size="33" text-anchor="middle" textLength="1000" lengthAdjust="spacing">FINANCIAL HACKS WITH SOME SOUTHERN CHARM</text>

  <text class="label-podcast" x="603" y="922" font-size="46" text-anchor="middle" letter-spacing="22">PODCAST</text>
  <text class="label-with" x="600" y="1036" font-size="96" text-anchor="middle">with</text>
  <text class="hosts" x="159" y="1101" font-size="48" textLength="886" lengthAdjust="spacing">WADE HARLAN &amp; COLE BENTON</text>
</svg>
</body>
</html>
```